Dietary supplement, Clean and simple.

Hi,
I’d like to talk about the project,

About us:
We are a dietary supplement (Vitamins, Minerals, amino acids etc.) company.
The goal is to have about 25 products at the end of this year. However, for this goal to be achieved we need a good label design to make our products represent our company values.
I’ll be here every day supporting your questions, we are fully committed to making the highest/best quality/customer experience possible.

About the design and our values:
- Professional (We are in the industry of professionalism and expertise. I would love to show we are competent at this, Id. Like to have the labels looks like we have done our research.)
- Efficient (White spacing, good use of the space available.)
- Simple (Straight forward, in 5 seconds they have to know what the product they have is/how functions. We’re trying to simplify it for the consumer.
- No distractions (the only visually “distracting” factor can be the vector art.)

The guidelines:
The goal is to have a universal design, with one element that changes (Vector art). I’ll attach a file/multiple files I think can show some visuals on what I’m looking for, and what parts of the design I think are good/bad.

Label size: 69x155mm (Front is 77.5mm)

Design whatever you think fits our image. You’re the design expert, all I care about is that it fits our company standards/image.

Use this color/font.
Font: Sans Serif
Main company color is Mind green #237D62 (Use this color for something in the design.)

What I thought would be cool/might looks ugly, who knows:
1. The front of the label: Should have 1 vector art, preferably in the top right corner. (That looks good in multiple colors. The vector can have multiple areas to color, I would prefer 2 main colors in the vector art. The interchangeable colors are used for multiple kinds of products.)
2. Text/product information on the left. The text that will have to be displayed:
- Product name for instance “Magnesium + B6”
- Description for the product for instance “Magnesium with ginger taste”
- Company name or logo. (Add ® behind it. We are soon to be trademark registered.)
3. We need to show the "daily intake" amount on the front and also the amount in the complete bottle. For instance, “Daily intake 1 capsule, 60 capsules”.
• You don’t have to design the backside of the label. After I chose a design, I’d like to chat and give specific information on what areas need to be assigned where. (Too complex because of the law.)
Updates

Hi, Please make the deadline 31 days total. I want designers to have the time to design. And not be rushed to finish it.

I want to extend the deadline because i feel like a slightly more medical look would be interesting. Hope you can come up with something!!

Target Market(s)

Dietary supplement consumers

Industry/Entity Type

Dietary supplements

Font styles to use
Sans Serif

Colors

Designer to choose colors to be used in the design.

Requirements
Must have
• Trademark icon "®" has to be at the top right after the company logo(text of logo)/name.

```html
<!DOCTYPE html>
<html lang="en">
<head>
<meta charset="UTF-8">
<title>Noble Calm – Magnesium + B6 label</title>
<link href="https://fonts.googleapis.com/css2?family=IBM+Plex+Sans:wght@400;500;600&display=swap" rel="stylesheet">
<style>
  :root {
    --bg: #ececec;
    --label: #f7f7f7;
    --ink: #1e1e1e;
    --ink-soft: #3c3c3c;
    --ink-grey: #5a5a5a;
    --mind-green: #237D62;
    --accent-pink: #e9b3c2;
    --accent-violet: #8a62a8;
    --accent-navy: #33358a;
  }
  * { margin: 0; padding: 0; box-sizing: border-box; }
  html, body {
    width: 1200px; height: 1200px; overflow: hidden;
    background: var(--bg);
    font-family: "IBM Plex Sans", Arial, sans-serif;
  }
  .label {
    position: absolute; left: 100px; top: 80px;
    width: 1000px; height: 1040px;
    background: var(--label);
    border-radius: 6px;
    box-shadow: 0 2px 10px rgba(0,0,0,0.05);
  }
  .hero-art {
    position: absolute; left: 60px; top: 60px;
    width: 320px; height: 500px;
    background:
      linear-gradient(200deg, rgba(233,179,194,1) 0%, rgba(233,179,194,0) 55%),
      linear-gradient(20deg, var(--accent-navy) 0%, var(--accent-violet) 50%, #c7a3c4 100%);
  }
  .brand-mark {
    position: absolute; right: 70px; top: 110px;
    display: flex; align-items: center; gap: 10px;
    color: var(--mind-green);
    font-weight: 600; font-size: 30px; letter-spacing: 1px;
  }
  .brand-mark .dot {
    width: 16px; height: 16px; border-radius: 50%;
    background: var(--mind-green);
  }
  .brand-line {
    position: absolute; left: 60px; top: 590px;
    font-size: 40px; font-weight: 400; color: var(--ink-soft);
    letter-spacing: 0.5px;
  }
  .brand-line sup { font-size: 22px; vertical-align: top; margin-left: 8px; }
  .product-name {
    position: absolute; left: 60px; top: 648px;
    font-size: 86px; font-weight: 600; color: var(--ink);
    letter-spacing: -0.5px; line-height: 1;
  }
  .product-name .plus { color: var(--ink-grey); }
  .rule {
    position: absolute; left: 60px; top: 775px;
    width: 320px; height: 6px;
    background: linear-gradient(90deg, var(--accent-pink), var(--accent-violet));
  }
  .description {
    position: absolute; left: 60px; top: 800px;
    font-size: 46px; font-weight: 400; color: var(--ink-soft);
    line-height: 1.18;
  }
  .divider {
    position: absolute; left: 60px; right: 60px; top: 935px;
    border-top: 2px dashed var(--mind-green);
    opacity: 0.7;
  }
  .count {
    position: absolute; left: 60px; top: 958px;
    display: flex; align-items: center; gap: 16px;
  }
  .count-text { font-size: 22px; line-height: 1.25; color: var(--ink-soft); }
  .count-text strong { color: var(--mind-green); font-weight: 600; display: block; }
  .intake {
    position: absolute; right: 60px; top: 958px;
    display: flex; align-items: stretch; gap: 14px;
    text-align: right;
  }
  .intake-text { font-size: 22px; line-height: 1.25; color: var(--ink-soft); }
  .intake-text strong { color: var(--mind-green); font-weight: 600; display: block; }
  .intake-bar { width: 3px; background: var(--mind-green); }
</style>
</head>
<body>
  <main class="label">
    <div class="hero-art" role="img" aria-label="Product vector art area in pink to navy gradient"></div>

    <div class="brand-mark"><span class="dot"></span>NOBLE CALM</div>

    <p class="brand-line">NOBLE CALM<sup>®</sup></p>
    <h1 class="product-name">Magnesium <span class="plus">+ B6</span></h1>
    <div class="rule"></div>
    <p class="description">Magnesium with<br>ginger taste</p>

    <div class="divider"></div>

    <div class="count">
      <svg width="30" height="60" viewBox="0 0 30 60" aria-hidden="true">
        <rect x="2" y="2" width="26" height="56" rx="13" fill="none" stroke="#237D62" stroke-width="3"/>
        <line x1="2" y1="30" x2="28" y2="30" stroke="#237D62" stroke-width="3"/>
      </svg>
      <p class="count-text"><strong>60</strong>CAPSULES</p>
    </div>

    <div class="intake">
      <p class="intake-text">DAILY INTAKE<strong>1 CAPSULE</strong></p>
      <span class="intake-bar"></span>
    </div>
  </main>
</body>
</html>
```